Atelier Greta Voss Coming Soon

Launching a online mid century furniture business. I'm participating in an antiques fair prior to the website launch. I'd like a 1 page flyer that highlights a sampling of some iconic pieces and invites people to check out the website soon. If possible, I'd also like a Word template for a tear sheet (a one page doc that has the company logo and contact info, a picture of the item, a field for description and dimensions). The following is an example of a tear sheet...http://www.kbtcabinetworks.example/uploads/4/8/1/3/4813902/vesper_oak_low_side_chair.pdf. I'd prefer a smaller slot for the image (maybe one side of the page) and a much larger area for description and dimensions (as its vintage furniture I'll need to report on condition).

I've attached a few sample pieces of furniture, the company logo, contact information, and a room that included furniture from the business. The color palette for the business is orange, black, white and gray.

Target Market(s)

Potential Customers.....

Industry/Entity Type

Retail

Font styles to use
Other font styles liked:
• I think the fonts should be similar to the ones used in the logo and the business card (see attached)

Colors
f37122
1b1b1b
ebebeb

Requirements
Must have
• An elegant clean look and feel (although its a mid century furniture business I don't carry kitschy items...just really beautiful classic high-end pieces). It should highlight the beauty of the furniture and provide contact information.

```html
<!DOCTYPE html>
<html lang="en">
<head>
<meta charset="utf-8">
<title>Atelier Greta Voss – Coming Soon Flyer</title>
<link rel="stylesheet" href="https://fonts.googleapis.com/css2?family=Antonio:wght@200&family=Open+Sans:wght@300;400;600&display=swap">
<style>
  :root {
    --orange: #f37122;
    --black: #1b1b1b;
    --paper: #f7f7f7;
    --gray: #ebebeb;
    --white: #ffffff;
  }
  html, body { margin: 0; padding: 0; overflow: hidden; background: var(--gray); }
  .flyer {
    position: relative;
    width: 1200px;
    height: 910px;
    background: linear-gradient(180deg, var(--white), var(--paper));
    overflow: hidden;
    font-family: "Open Sans", Arial, sans-serif;
  }
  .flyer__shapes { position: absolute; inset: 0; width: 1200px; height: 910px; }
  .brand-name {
    position: absolute;
    margin: 0;
    font-family: "Antonio", "Arial Narrow", sans-serif;
    font-weight: 200;
    color: var(--black);
    white-space: nowrap;
    line-height: 1;
  }
  .brand-name--header { left: 112px; top: 40px; font-size: 116px; letter-spacing: 6px; }
  .brand-name--footer { right: 38px; top: 806px; font-size: 52px; letter-spacing: 2px; color: var(--orange); }
  .headline {
    position: absolute;
    left: 563px;
    top: 374px;
    width: 620px;
    margin: 0;
    text-align: center;
    font-weight: 300;
    font-size: 55px;
    line-height: 96px;
    text-transform: uppercase;
  }
  .headline span { display: block; white-space: nowrap; }
  .headline .accent { color: var(--orange); }
  .headline .light { color: var(--white); }
  .contact-name {
    position: absolute;
    left: 312px;
    top: 712px;
    margin: 0;
    font-size: 29px;
    font-weight: 300;
    color: var(--black);
  }
  .contact-name strong { font-weight: 400; }
  .contact-list {
    position: absolute;
    left: 129px;
    top: 778px;
    display: flex;
    margin: 0;
    padding: 0;
    list-style: none;
  }
  .contact-item {
    display: flex;
    flex-direction: column;
    align-items: center;
    box-sizing: border-box;
    height: 118px;
    padding: 0 6px;
    font-size: 15px;
    line-height: 20px;
    color: var(--black);
    text-align: left;
    white-space: nowrap;
  }
  .contact-item + .contact-item { border-left: 2px solid var(--black); }
  .contact-item svg { width: 46px; height: 46px; margin: 14px 0 10px; flex: none; }
  .contact-item--email { width: 216px; }
  .contact-item--phone { width: 184px; }
  .contact-item--web { width: 200px; }
</style>
</head>
<body>
<main class="flyer">
  <svg class="flyer__shapes" viewBox="170 150 942 673" preserveAspectRatio="none">
    <defs>
      <linearGradient id="roomTones" x1="0" y1="0" x2="1" y2="1">
        <stop offset="0" stop-color="#d9d2c6"/>
        <stop offset="0.45" stop-color="#b79e80"/>
        <stop offset="1" stop-color="#5d4c3e"/>
      </linearGradient>
    </defs>
    <path class="band-black" fill="#1b1b1b"
      d="M170,300 C300,282 430,296 540,366 C620,418 760,428 880,380 C970,342 1050,272 1112,196 L1112,650 C990,702 800,714 680,660 C600,622 540,606 170,700 Z"/>
    <path class="band-orange-top" fill="#f37122"
      d="M640,406 C840,396 1000,300 1080,150 L1112,150 L1112,180 C1020,322 850,404 640,406 Z"/>
    <path class="room-photo" role="img" aria-label="Photograph of a furnished living room with mid-century chairs, a dining table and lit shelves of art objects"
      fill="url(#roomTones)" stroke="#ffffff" stroke-width="4"
      d="M170,318 C300,298 410,328 470,388 C522,440 544,522 612,610 C480,612 300,640 170,702 Z"/>
    <path class="band-orange-bottom" fill="#f37122"
      d="M170,738 C300,660 450,616 612,612 C462,630 300,700 212,822 L170,822 Z"/>
  </svg>

  <h1 class="brand-name brand-name--header">ATELIER GRETA VOSS</h1>

  <h2 class="headline">
    <span class="accent">Check out</span>
    <span class="light">Our newly launch</span>
    <span class="accent">Website soon</span>
  </h2>

  <p class="contact-name">Lotte <strong>Brandvik</strong></p>

  <ul class="contact-list">
    <li class="contact-item contact-item--email">
      <svg viewBox="0 0 46 46" aria-hidden="true">
        <circle cx="23" cy="23" r="23" fill="#f37122"/>
        <rect x="11" y="15" width="24" height="16" fill="none" stroke="#fff" stroke-width="2.5"/>
        <path d="M11,15 L23,25 L35,15" fill="none" stroke="#fff" stroke-width="2.5"/>
      </svg>
      <span>lotte@ateliergretavoss.com</span>
    </li>
    <li class="contact-item contact-item--phone">
      <svg viewBox="0 0 46 46" aria-hidden="true">
        <circle cx="23" cy="23" r="23" fill="#1b1b1b"/>
        <path d="M15,12 L20,12 L22,18 L19,20 C20.5,24 22,25.5 26,27 L28,24 L34,26 L34,31 C34,33 32,34 30,34 C21,33 13,25 12,16 C12,14 13,12 15,12 Z" fill="#fff"/>
      </svg>
      <span>Office 312-555-0148<br>Mobile 312-555-0193</span>
    </li>
    <li class="contact-item contact-item--web">
      <svg viewBox="0 0 46 46" aria-hidden="true">
        <circle cx="23" cy="23" r="23" fill="#f37122"/>
        <g fill="none" stroke="#fff" stroke-width="2">
          <circle cx="23" cy="23" r="12"/>
          <ellipse cx="23" cy="23" rx="5" ry="12"/>
          <path d="M11,23 H35 M13,17 H33 M13,29 H33"/>
        </g>
      </svg>
      <span>www.ateliergretavoss.com</span>
    </li>
  </ul>

  <p class="brand-name brand-name--footer">ATELIER GRETA VOSS</p>
</main>
</body>
</html>
```